Harborline Energy - needs a business card

Harborline Energy is a U.S. based diesel sourcing and distribution company that supports American oil & gas fields through providing quality product and consistent services.

Target Market(s)

Oil and Gas

Contact Information for Business Card

The background of the card must be white to ensure the logo pops.

Font styles to use
Serif
Sans Serif

Colors

Designer to choose colors to be used in the design.

Requirements
Must have
• Front of Card: Tag line: Harborline Energy, Powering America's Oil & Gas fields.
• Not sure if you guys do this part but just in case...
• Dale Menschow
• Owner/CEO
• C:555.318.4076
• E:Dmenschow@harborlineenergy.example
• W:Harborlineenergy.example
• Locations: Servicing the Powder River, DJ basin and Bakken formations.
• Back of Card: " Frac fueling is what we do. We understand how important diesel fuel is to your operation, which is why our main service line is Frac fueling. We assure our supply and stand by our service"

```html
<!DOCTYPE html>
<html lang="en">
<head>
<meta charset="utf-8">
<title>Harborline Energy – Business Card</title>
<link href="https://fonts.googleapis.com/css2?family=Source+Sans+3:ital,wght@0,400;0,600;0,700;1,700&display=swap" rel="stylesheet">
<style>
  :root {
    --navy: #1e3156;
    --red: #b01c1f;
    --text: #2b3a55;
    --rule: #c9ccd3;
    --paper: #ffffff;
  }
  * { margin: 0; padding: 0; box-sizing: border-box; }
  html, body {
    width: 1000px; height: 1200px; overflow: hidden;
    background: var(--paper);
    font-family: "Source Sans 3", sans-serif;
  }
  .canvas { position: relative; width: 1000px; height: 1200px; }

  .card {
    position: absolute;
    left: 165px; width: 664px; height: 430px;
    border: 3px solid var(--navy);
    background: var(--paper);
    overflow: hidden;
  }
  .card--front { top: 124px; }
  .card--back { top: 634px; }

  /* Front */
  .brand-mark {
    position: absolute; left: 400px; top: 40px; width: 210px;
    text-align: center;
  }
  .brand-mark__dot {
    display: block; width: 74px; height: 74px; margin: 0 auto 14px;
    border-radius: 50%; background: var(--navy);
  }
  .brand-mark__name {
    color: var(--navy); font-weight: 700; font-size: 30px;
    line-height: 1.0; letter-spacing: 0.5px;
  }

  .person { position: absolute; left: 38px; top: 148px; }
  .person__name {
    color: var(--red); font-weight: 700; font-size: 35px; line-height: 1;
  }
  .person__title {
    color: var(--red); font-weight: 400; font-size: 21px; line-height: 1;
    margin-top: 9px;
  }
  .contact { list-style: none; margin-top: 8px; }
  .contact__item {
    display: flex; align-items: flex-start;
    color: var(--text); font-size: 16.5px; line-height: 28px;
  }
  .contact__icon {
    width: 18px; height: 18px; margin: 5px 6px 0 0; flex: none;
  }

  .front-rule {
    position: absolute; left: 0; right: 0; top: 372px;
    height: 2px; background: var(--rule);
  }
  .tagline {
    position: absolute; left: 0; right: 0; top: 388px;
    text-align: center; color: var(--navy);
    font-weight: 700; font-size: 21.5px;
  }
  .tagline__brand { color: var(--red); }

  /* Back */
  .emblem-art {
    position: absolute; left: 0; top: 12px; width: 240px; height: 412px;
    background: linear-gradient(160deg, var(--navy) 0%, var(--red) 45%, var(--navy) 100%);
    border-radius: 0 60% 40% 0;
  }
  .pledge {
    position: absolute; left: 270px; top: 196px;
    color: var(--navy); font-weight: 700; font-style: italic;
    font-size: 17px; line-height: 22px; white-space: nowrap;
  }
  .pledge__lead { color: var(--red); }
</style>
</head>
<body>
<main class="canvas">

  <section class="card card--front" aria-label="Card front">
    <div class="brand-mark">
      <span class="brand-mark__dot"></span>
      <div class="brand-mark__name">Harborline<br>Energy</div>
    </div>

    <div class="person">
      <h1 class="person__name">Dale Menschow</h1>
      <p class="person__title">Owner/CEO</p>
      <ul class="contact">
        <li class="contact__item">
          <svg class="contact__icon" viewBox="0 0 18 18"><rect x="4" y="0.5" width="10" height="17" rx="2.5" fill="var(--red)"/><rect x="6" y="3" width="6" height="7" fill="#fff"/><circle cx="9" cy="14" r="1.4" fill="#fff"/></svg>
          555.318.4076
        </li>
        <li class="contact__item">
          <svg class="contact__icon" viewBox="0 0 18 18"><rect x="1" y="4" width="16" height="11" fill="none" stroke="var(--red)" stroke-width="1.6"/><path d="M1 4 L9 10.5 L17 4 M1 15 L7 9 M17 15 L11 9" fill="none" stroke="var(--red)" stroke-width="1.4"/></svg>
          Dmenschow@harborlineenergy.example
        </li>
        <li class="contact__item">
          <svg class="contact__icon" viewBox="0 0 18 18" fill="none" stroke="var(--red)" stroke-width="1.3"><circle cx="9" cy="9" r="7.5"/><ellipse cx="9" cy="9" rx="3.3" ry="7.5"/><path d="M1.5 9 H16.5 M2.8 5 H15.2 M2.8 13 H15.2"/></svg>
          Harborlineenergy.example
        </li>
        <li class="contact__item">
          <svg class="contact__icon" viewBox="0 0 18 18"><path d="M9 0.5 C5 0.5 2.5 3.5 2.5 6.8 C2.5 11 9 17.5 9 17.5 C9 17.5 15.5 11 15.5 6.8 C15.5 3.5 13 0.5 9 0.5 Z" fill="var(--red)"/><circle cx="9" cy="6.8" r="2.4" fill="#fff"/></svg>
          <span>Servicing the Powder River,<br>DJ basin and Bakken formations</span>
        </li>
      </ul>
    </div>

    <div class="front-rule"></div>
    <p class="tagline"><span class="tagline__brand">Harborline Energy</span>, Powering America's Oil &amp; Gas fields.</p>
  </section>

  <section class="card card--back" aria-label="Card back">
    <div class="emblem-art" role="img" aria-label="Large stylised red and navy eagle head emblem"></div>
    <p class="pledge">" <span class="pledge__lead">Frac fueling</span> is what we do. We understand<br>how important diesel fuel is to your operation,<br>which is why our main service line is Frac fueling.<br>We assure our supply and stand by our service"</p>
  </section>

</main>
</body>
</html>
```